Flyer design for company which solely specializes in transferring Videos to DVD

I would like a flyer designed for my small business i own a digital transferring business which solely specializes in transferring videos to DVD.

My company is called tapesavedisc.

This flyer will be going through peoples doors and will be my first impression of the company. It needs to make them call me and transfer their videos.

In the must have section i have included a few lines of text i would like to include, please take any other information you think is necessary from my website and include it.

The flyer will be size A5 and double sided!

Target Market(s)

age group 30+ who want their home movies transferred on to DVD

Industry/Entity Type

Small Business

Requirements
Must have
• The flyer must include:

Company Logo - attached image

Headline of - Take action don't lose your precious home movies!

Did you know the average video tape has a shelf life of between 15-20 years, after this time period the quality starts to degrade.

Here at Tapesavedisc we offer a specialist service in transferring videos to DVD.

We pride ourselves on being the cheapest and best service in the whole of the UK.

There are no expensive postage fees as we hand collect and deliver your videos free of charge!

Prices:
Transfer for first copy = £7
Additional copies = £3

Order before July 31st and receive 10% off.

Order now either by telephone on 07912638405 or email tapesavedisc@mailbrook.co.uk.

For more information go to our website address www.tapesavedisc-example.co.uk

Testimonials

"Your service was brilliant the DVD’s were of the highest quality and the lowest price I have come across, I will be recommending you to all my friends!"

Gareth from Midsomer Norton

"Just wanted to say thanks for an amazing service, it was super fast and it’s brilliant to see the old family movies which we haven’t seen for years!!!"

Wendy from Midsomer Norton
Nice to have
• I would like the color scheme to be orange black and white as this is the colors of my website. However i am happy to try different colors and i am very open minded.

The website is currently under.
www.tapesavedisc-example.co.uk

```html
<!DOCTYPE html>
<html lang="en">
<head>
<meta charset="utf-8">
<title>Tapesavedisc – A5 Flyer, Front and Back</title>
<link href="https://fonts.googleapis.com/css2?family=PT+Sans+Narrow:wght@400;700&family=Kaushan+Script&family=Salsa&display=swap" rel="stylesheet">
<style>
  :root {
    --ink: #231f20;
    --orange: #f7941d;
    --orange-deep: #f26d21;
    --blue: #29abe2;
    --blue-deep: #1b75bc;
    --yellow: #ffe600;
    --white: #ffffff;
    --grey-light: #e6e7e8;
    --grey-mid: #a7a9ac;
    --grey-dark: #58595b;
    --backdrop: #d8d6d2;
  }
  * { box-sizing: border-box; margin: 0; padding: 0; }
  html, body { width: 1200px; height: 849px; overflow: hidden; }
  body {
    background: var(--backdrop);
    font-family: "PT Sans Narrow", "Arial Narrow", sans-serif;
    position: relative;
  }
  .flyer {
    position: absolute;
    top: 75px;
    width: 495px;
    height: 700px;
    overflow: hidden;
    box-shadow: 0 6px 18px rgba(0,0,0,.25);
  }
  .flyer--front { left: 90px; background: var(--ink); color: var(--white); }
  .flyer--back  { left: 615px; background: var(--orange); color: var(--ink); }
  .abs { position: absolute; }

  /* ---------- Front ---------- */
  .brand-frame {
    left: 25px; top: 25px; width: 445px; height: 95px;
    border: 4px solid var(--white); border-radius: 22px;
    background: linear-gradient(180deg, #6d6e71, #3a3a3c);
    display: flex; align-items: center; justify-content: center;
  }
  .brand-name {
    font-weight: 700; font-size: 40px; letter-spacing: 1px;
    color: var(--orange); text-transform: uppercase;
  }
  .headline {
    left: 20px; top: 130px; width: 455px; text-align: center;
    font-weight: 700; font-size: 40px; line-height: 1.05;
  }
  .headline__lead { color: var(--orange); }
  .fact-bulb {
    left: 28px; top: 232px; width: 38px; height: 50px; border-radius: 50% 50% 30% 30%;
    background: radial-gradient(circle at 45% 40%, #fff6c0, #f6c945 60%, #b58b1a);
  }
  .fact {
    left: 75px; top: 232px; width: 395px;
    border-bottom: 2px dotted var(--white); padding-bottom: 6px;
  }
  .fact__title {
    font-family: "Kaushan Script", cursive; color: var(--blue); font-size: 20px;
    border-bottom: 2px dotted var(--white); padding-bottom: 2px; margin-bottom: 4px;
  }
  .fact__text { font-size: 15px; line-height: 1.25; }
  .intro {
    left: 20px; top: 322px; width: 455px; text-align: center;
    font-size: 12.5px; line-height: 1.9;
  }
  .intro__brand { color: var(--orange); font-weight: 700; font-size: 17px; text-transform: uppercase; }
  .price-band {
    left: 0; top: 455px; width: 310px; height: 64px;
    background: linear-gradient(90deg, var(--orange), var(--orange-deep));
    border-radius: 0 12px 12px 0;
    display: flex; align-items: center; padding-left: 12px; gap: 8px;
  }
  .price-band__label {
    writing-mode: vertical-rl; transform: rotate(180deg);
    font-size: 11px; font-weight: 700; color: #ffd9a8; letter-spacing: 1px;
  }
  .price-band__list { font-weight: 700; font-size: 19px; line-height: 1.25; }
  .price-band__list span { color: var(--white); }
  .price-band__list { color: var(--ink); }
  .contact { left: 28px; top: 545px; width: 260px; font-size: 12px; line-height: 1.35; }
  .contact__hi { color: var(--orange); font-weight: 700; font-size: 17px; }
  .contact__web { margin-top: 18px; }
  .contact__url { color: var(--blue); font-weight: 700; font-size: 19px; }
  .film-art {
    left: 330px; top: 430px; width: 165px; height: 95px;
    background: linear-gradient(135deg, #5a5b5d, #2b2b2d 60%, #8c8e91);
  }
  .swoosh { left: 0; bottom: 0; width: 495px; height: 150px; }

  .badge { width: 180px; height: 180px; }
  .badge svg { position: absolute; inset: 0; width: 100%; height: 100%; }
  .badge__text {
    position: absolute; inset: 0; display: flex; flex-direction: column;
    align-items: center; justify-content: center; text-align: center;
    color: var(--white); font-weight: 700; font-size: 15px; line-height: 1.05;
  }
  .badge__offer { color: var(--yellow); font-size: 38px; margin-top: 4px; }
  .flyer--front .badge { left: 305px; top: 515px; }

  /* ---------- Back ---------- */
  .back-bg { left: 0; top: 0; width: 495px; height: 700px; }
  .back-contact {
    right: 22px; top: 22px; text-align: right; color: var(--white);
    font-size: 12px; line-height: 1.35;
  }
  .back-contact__hi { color: var(--blue); font-weight: 700; font-size: 17px; }
  .bubble { left: 18px; top: 22px; width: 175px; height: 100px; }
  .bubble__label {
    position: absolute; left: 0; top: 18px; width: 175px; text-align: center;
    font-family: "Salsa", cursive; font-size: 22px; color: var(--ink);
  }
  .quotes {
    left: 35px; top: 145px; width: 435px; height: 265px;
    background: linear-gradient(180deg, #f1f2f2, var(--grey-mid));
    border-radius: 12px; padding: 18px 22px 10px 40px; color: var(--ink);
  }
  .quote { position: relative; margin-bottom: 12px; }
  .quote__text { font-size: 11.5px; line-height: 1.35; }
  .quote__mark {
    position: absolute; font-family: Georgia, serif; font-weight: 700;
    font-size: 42px; line-height: 1; color: var(--ink);
  }
  .quote__mark--open { left: -30px; top: -6px; }
  .quote__mark--close { right: -14px; bottom: 4px; }
  .quote__by {
    text-align: right; text-transform: uppercase; font-size: 10px;
    color: var(--grey-dark); margin-top: 3px; letter-spacing: .3px;
  }
  .flyer--back .film-art { left: 0; top: 375px; width: 150px; height: 115px; }
  .flyer--back .badge { left: 95px; top: 420px; width: 160px; height: 160px; }
  .flyer--back .badge__text { font-size: 13px; }
  .flyer--back .badge__offer { font-size: 33px; }
  .tape-art {
    left: 250px; top: 470px; width: 225px; height: 100px; border-radius: 6px;
    background: linear-gradient(160deg, #6d6e71, #2b2b2d);
  }
  .format-icons { right: 25px; top: 585px; width: 95px; height: 38px; }
  .back-brand {
    right: 25px; top: 628px; font-weight: 700; font-size: 24px;
    color: var(--ink); text-transform: uppercase;
  }
  .back-url {
    left: 0; bottom: 12px; width: 495px; text-align: center;
    font-weight: 700; font-size: 33px; color: var(--ink);
  }
</style>
</head>
<body>

<section class="flyer flyer--front">
  <svg class="abs swoosh" viewBox="0 0 495 150" aria-hidden="true">
    <path d="M0 150 L0 120 C140 70 320 40 495 30 L495 150 Z" fill="#3a3a3c"/>
    <path d="M0 150 C160 105 330 80 495 75 L495 150 Z" fill="#58595b"/>
  </svg>

  <div class="abs brand-frame"><span class="brand-name">Tapesavedisc</span></div>

  <h1 class="abs headline"><span class="headline__lead">Take Action:</span> Don’t lose your precious home movies!</h1>

  <div class="abs fact-bulb" role="img" aria-label="Glowing light bulb illustration"></div>
  <div class="abs fact">
    <p class="fact__title">Did you know?</p>
    <p class="fact__text">The average video tape has a shelf life of between 15-20 years, after this time period the quality starts to degrade.</p>
  </div>

  <div class="abs intro">
    <p>Here at <span class="intro__brand">Tapesavedisc</span> we offer a specialist service in transferring videos to DVD.</p>
    <p>We pride ourselves on being the cheapest and best service in the whole of the UK.</p>
    <p>There are no expensive postage fees as we hand collect and deliver your videos free of charge!</p>
  </div>

  <div class="abs price-band">
    <span class="price-band__label">PRICES</span>
    <p class="price-band__list">Transfer for first copy: <span>£7</span><br>Additional copies: <span>£3</span></p>
  </div>

  <div class="abs film-art" role="img" aria-label="Curling strip of film illustration"></div>

  <div class="abs contact">
    <p>Order now either by telephone on</p>
    <p><span class="contact__hi">07912638405</span> or email</p>
    <p class="contact__hi">tapesavedisc@mailbrook.co.uk</p>
    <p class="contact__web">For more information go to our website</p>
    <p class="contact__url">www.tapesavedisc-example.co.uk</p>
  </div>

  <div class="abs badge">
    <svg viewBox="-105 -105 210 210" aria-hidden="true">
      <defs>
        <radialGradient id="badgeFill" cx="40%" cy="35%" r="70%">
          <stop offset="0" stop-color="#5cc6f0"/>
          <stop offset="1" stop-color="#1b75bc"/>
        </radialGradient>
        <symbol id="starburst" viewBox="-105 -105 210 210">
          <polygon fill="#ffffff" points="100,0 88.3,17.6 92.4,38.3 74.8,50 70.7,70.7 50,74.8 38.3,92.4 17.6,88.3 0,100 -17.6,88.3 -38.3,92.4 -50,74.8 -70.7,70.7 -74.8,50 -92.4,38.3 -88.3,17.6 -100,0 -88.3,-17.6 -92.4,-38.3 -74.8,-50 -70.7,-70.7 -50,-74.8 -38.3,-92.4 -17.6,-88.3 0,-100 17.6,-88.3 38.3,-92.4 50,-74.8 70.7,-70.7 74.8,-50 92.4,-38.3 88.3,-17.6"/>
          <circle r="80" fill="url(#badgeFill)"/>
        </symbol>
      </defs>
      <use href="#starburst" x="-105" y="-105" width="210" height="210"/>
    </svg>
    <div class="badge__text">
      <span>Order before</span><span>July 31st 2012</span><span>and receive</span>
      <span class="badge__offer">10% OFF</span>
    </div>
  </div>
</section>

<section class="flyer flyer--back">
  <svg class="abs back-bg" viewBox="0 0 495 700" aria-hidden="true">
    <path d="M0 0 H495 V115 C360 125 200 150 0 215 Z" fill="#231f20"/>
    <path d="M175 150 C300 125 400 115 495 112 V126 C400 130 300 140 190 160 Z" fill="#fbb040"/>
  </svg>

  <div class="abs back-contact">
    <p>Order now either by telephone on</p>
    <p><span class="back-contact__hi">07912638405</span> or email</p>
    <p class="back-contact__hi">tapesavedisc@mailbrook.co.uk</p>
  </div>

  <div class="abs bubble">
    <svg width="175" height="100" viewBox="0 0 175 100" aria-hidden="true">
      <path d="M87 4 C140 4 171 20 171 38 C171 58 140 72 110 72 L118 96 L88 72 C40 72 4 58 4 38 C4 20 35 4 87 4 Z" fill="#ffffff" stroke="#231f20" stroke-width="3"/>
    </svg>
    <span class="bubble__label">Testimonials</span>
  </div>

  <div class="abs quotes">
    <div class="quote">
      <span class="quote__mark quote__mark--open">“</span>
      <p class="quote__text">Your service was brilliant the DVD’s were of the highest quality and the lowest price I have come across, I will be recommending you to all my friends!</p>
      <span class="quote__mark quote__mark--close">”</span>
      <p class="quote__by">Gareth from Midsomer Norton</p>
    </div>
    <div class="quote">
      <span class="quote__mark quote__mark--open">“</span>
      <p class="quote__text">Just wanted to say thanks for an amazing service, it was super fast and it’s brilliant to see the old family movies which we haven’t seen for years!!!</p>
      <span class="quote__mark quote__mark--close">”</span>
      <p class="quote__by">Wendy from Midsomer Norton</p>
    </div>
    <div class="quote">
      <span class="quote__mark quote__mark--open">“</span>
      <p class="quote__text">It was fantastic to be able to view the footage from a 15 year old VHS tape. It was brilliant to watch my daughter see herself for the first time as a toddler.</p>
      <span class="quote__mark quote__mark--close">”</span>
      <p class="quote__by">Helen from Farrington Gurney</p>
    </div>
  </div>

  <div class="abs film-art" role="img" aria-label="Curling strip of film illustration"></div>

  <div class="abs badge">
    <svg viewBox="-105 -105 210 210" aria-hidden="true">
      <use href="#starburst" x="-105" y="-105" width="210" height="210"/>
    </svg>
    <div class="badge__text">
      <span>Order before</span><span>July 31st 2012</span><span>and receive</span>
      <span class="badge__offer">10% OFF</span>
    </div>
  </div>

  <div class="abs tape-art" role="img" aria-label="Video cassette with unspooling tape illustration"></div>
  <div class="abs format-icons" role="img" aria-label="Tape to disc conversion icons" style="background: linear-gradient(90deg, #231f20 0 38%, transparent 38% 62%, #231f20 62%); border-radius: 4px;"></div>

  <p class="abs back-brand">Tapesavedisc</p>
  <p class="abs back-url">www.tapesavedisc-example.co.uk</p>
</section>

</body>
</html>
```